Fitness Clothing Apparel Business Card

This project is linked to Fitness Clothing Apparel, KESTREL, Looking for AWESOME Logo Design!!!.

Our company needs a Business Card Design. Please refer to our original project in the link above.

Hi, I'm looking for a professional logo design which will help brand my clothing and nutrition supplement company. The winner of this contest may be hired again in the future to help design some flyers, banners, graphics, etc.

A little background about the company...
KESTREL Fitness is a new fitness clothing and nutrition company based in Southern California... near the mecca of bodybuilding, Harlow Strand! Our company is based around the culture of fitness and bodybuilding. We design clothing that are functional yet appealing for an athletic individual.

What I would like to see on business card...
The card has communicate our brand values. It needs to have attitude yet professionally done. Our brand colors are black, red, and white.

Target Market(s)

Fitness and bodybuilding enthusiasts

Industry/Entity Type

Nutrition

Font styles to use
Serif
Sans Serif
Decorative
Script

Colors

Designer to choose colors to be used in the design.

Requirements
Must have
• our company logo
Nice to have
• red and black, an abstract design of a bull
Should not have
• I'm open to all ideas, appearance is important

```html
<!DOCTYPE html>
<html lang="en">
<head>
<meta charset="utf-8">
<title>KESTREL Business Card</title>
<link rel="stylesheet" href="https://fonts.googleapis.com/css2?family=Questrial&family=Arimo&display=swap">
<style>
  :root {
    --canvas: #ffffff;
    --card: #000000;
    --ink: #ffffff;
  }
  html, body {
    margin: 0;
    padding: 0;
    width: 1200px;
    height: 1200px;
    overflow: hidden;
    background: var(--canvas);
  }
  .canvas {
    position: relative;
    width: 1200px;
    height: 1200px;
    background: var(--canvas);
  }
  .card {
    position: absolute;
    left: 294px;
    width: 635px;
    height: 366px;
    background: var(--card);
    color: var(--ink);
  }
  .card--front { top: 244px; }
  .card--back { top: 666px; }

  .brand-name {
    position: absolute;
    font-family: "Questrial", sans-serif;
    font-weight: 400;
    color: var(--ink);
    white-space: nowrap;
    margin: 0;
  }
  .card--front .brand-name {
    left: 0;
    right: 0;
    top: 154px;
    text-align: center;
    font-size: 52px;
    letter-spacing: 12px;
    padding-left: 12px;
  }
  .card--back .brand-name {
    left: 42px;
    width: 260px;
    top: 216px;
    text-align: center;
    font-size: 30px;
    letter-spacing: 8px;
  }

  .contact {
    position: absolute;
    right: 44px;
    top: 80px;
    text-align: right;
  }
  .contact__name {
    margin: 0 0 22px;
    font-family: "Questrial", sans-serif;
    font-weight: 400;
    font-size: 29px;
    letter-spacing: 2px;
    line-height: 1;
  }
  .contact__group {
    margin: 0 0 30px;
    font-family: "Arimo", sans-serif;
    font-size: 22.5px;
    line-height: 30px;
    font-style: normal;
  }
  .contact__group:last-child { margin-bottom: 0; }
</style>
</head>
<body>
<main class="canvas">
  <section class="card card--front" aria-label="Card front">
    <p class="brand-name">KESTREL</p>
  </section>

  <section class="card card--back" aria-label="Card back">
    <p class="brand-name">KESTREL</p>
    <div class="contact">
      <h1 class="contact__name">DANA REYES</h1>
      <address class="contact__group">
        333 address<br>
        city, state, 55555
      </address>
      <address class="contact__group">
        555.555.5555<br>
        DReyes@website.com<br>
        www.website.com
      </address>
    </div>
  </section>
</main>
</body>
</html>
```